Quenby Bespoke Furnishings logo and business card

Quenby is a female operated furniture design and reupholstery business. Working with luxury top end fabrics and furnishings for unique and stylish one off designs. Bringing loved pieces of furniture back to life by recovering on modern, trendy, stylish fabrics. Think Velvet chaise lounge or velour Chesterfield lounges, vibrant and unique colourful, individually designed statement pieces.
We would like a simple logo that can be used on socials and a business card that is simple yet striking . Possibly using a bronze or gold foil.
The business name is QUENBY BESPOKE FURNISHINGS
Can be just QUENBY
Logo will be used on socials and images of finished furniture.

Target Market(s)

high end luxury holiday houses. Artistic flair designer houses

Industry/Entity Type

Home Furniture

Contact Information for Business Card

Simple yet designer
Logo on the front and name details on the back

Font styles to use
Decorative

Requirements
Must have
• Finess
A feel of artistic design
Just a logo/business name on the front of the card
Should not have
• not a picture of furniture

```html
<!DOCTYPE html>
<html lang="en">
<head>
<meta charset="utf-8">
<title>Quenby Bespoke Furnishings – Business Card</title>
<link href="https://fonts.googleapis.com/css2?family=Poppins:wght@400;500;600&display=swap" rel="stylesheet">
<style>
  :root {
    --backdrop: #2a2a2a;
    --card-black: #0d0d0d;
    --gold: #c99a3c;
    --gold-light: #f0cf6a;
    --gold-deep: #a7772a;
    --silver: #d9d9d9;
    --silver-dark: #8c8c8c;
    --paper: #ffffff;
    --ink: #111111;
  }
  * { margin: 0; padding: 0; box-sizing: border-box; }
  html, body {
    width: 1200px; height: 900px; overflow: hidden;
    background: var(--backdrop);
    font-family: "Poppins", sans-serif;
  }
  .stage {
    position: relative; width: 1200px; height: 900px;
  }
  .card {
    position: absolute; left: 250px; width: 700px; height: 400px;
    border-radius: 22px; overflow: hidden;
    box-shadow: 0 14px 34px rgba(0,0,0,.55);
  }
  .card-front { top: 40px; background: var(--card-black); }
  .card-back { top: 468px; background: var(--paper); }

  .front-rule {
    position: absolute; left: 0; right: 0; bottom: 42px; height: 3px;
    background: var(--gold);
  }
  .wordmark {
    position: absolute; text-align: center; color: var(--gold);
    font-weight: 500; line-height: 1;
  }
  .card-front .wordmark { left: 0; right: 0; top: 140px; }
  .wordmark .name { font-size: 64px; letter-spacing: 8px; display: block; }
  .wordmark .tagline { font-size: 13px; letter-spacing: 5px; display: block; margin-top: 12px; }

  .back-art { position: absolute; inset: 0; width: 700px; height: 400px; }
  .card-back .wordmark { left: 60px; width: 330px; top: 52px; }
  .card-back .wordmark .name { font-size: 50px; letter-spacing: 6px; }
  .card-back .wordmark .tagline { font-size: 11px; letter-spacing: 4px; margin-top: 10px; }

  .address {
    position: absolute; left: 48px; top: 166px;
    color: var(--gold); font-size: 14.5px; line-height: 1.45; font-weight: 500;
  }
  .contact-list {
    position: absolute; left: 48px; top: 248px; list-style: none;
    color: var(--gold); font-size: 15px; font-weight: 500;
  }
  .contact-list li { display: flex; align-items: center; gap: 10px; height: 26px; }
  .contact-list svg { width: 15px; height: 15px; fill: none; stroke: var(--gold); stroke-width: 1.8; }

  .person {
    position: absolute; right: 40px; top: 178px; text-align: right; color: var(--ink);
  }
  .person .person-name { font-size: 25px; font-weight: 600; }
  .person .person-role { font-size: 15px; font-weight: 500; margin-top: 2px; }
</style>
</head>
<body>
<main class="stage">
  <section class="card card-front">
    <div class="wordmark">
      <span class="name">QUENBY</span>
      <span class="tagline">BESPOKE FURNISHINGS</span>
    </div>
    <div class="front-rule"></div>
  </section>

  <section class="card card-back">
    <svg class="back-art" viewBox="0 0 700 400" aria-hidden="true">
      <defs>
        <linearGradient id="goldSweep" x1="0" y1="0" x2="1" y2="1">
          <stop offset="0" stop-color="var(--gold-light)"/>
          <stop offset=".5" stop-color="var(--gold)"/>
          <stop offset="1" stop-color="var(--gold-deep)"/>
        </linearGradient>
        <linearGradient id="silverSweep" x1="0" y1="0" x2="1" y2="0">
          <stop offset="0" stop-color="var(--silver-dark)"/>
          <stop offset=".5" stop-color="#ffffff"/>
          <stop offset="1" stop-color="var(--silver)"/>
        </linearGradient>
      </defs>
      <path d="M500,0 H560 C520,130 470,300 330,400 H250 C400,320 470,150 500,0 Z" fill="url(#goldSweep)"/>
      <path d="M455,0 H500 C470,140 410,310 260,400 H170 C340,330 425,150 455,0 Z" fill="#111"/>
      <path d="M430,0 H470 C440,140 380,310 220,400 H120 C300,330 400,150 430,0 Z" fill="url(#silverSweep)"/>
      <path d="M0,0 H440 C405,150 330,320 160,370 C100,385 40,388 0,386 Z" fill="var(--card-black)"/>
      <path d="M425,0 C395,150 330,330 200,380" fill="none" stroke="var(--gold)" stroke-width="1.5"/>
    </svg>

    <div class="wordmark">
      <span class="name">QUENBY</span>
      <span class="tagline">BESPOKE FURNISHINGS</span>
    </div>

    <address class="address" style="font-style:normal">
      418 Harlow Street NE<br>
      Suite 210, Aldermoor<br>
      MI 49821
    </address>

    <ul class="contact-list">
      <li><svg viewBox="0 0 16 16"><path d="M4 2 L6.5 5 L5 6.5 C6 8.5 7.5 10 9.5 11 L11 9.5 L14 12 L12 14 C7 13 3 9 2 4 Z"/></svg>555-014-2783</li>
      <li><svg viewBox="0 0 16 16"><rect x="1.5" y="3.5" width="13" height="9"/><path d="M1.5 3.5 L8 9 L14.5 3.5"/></svg>everett@quenbybe.com</li>
      <li><svg viewBox="0 0 16 16"><circle cx="8" cy="8" r="6.5"/><path d="M1.5 8 H14.5 M8 1.5 C5 5 5 11 8 14.5 C11 11 11 5 8 1.5"/></svg>www.quenby.com</li>
    </ul>

    <div class="person">
      <div class="person-name">Everett Lindqvist</div>
      <div class="person-role">CEO/Founder</div>
    </div>
  </section>
</main>
</body>
</html>
```